Eye surgeon needs a presentation folder and a business card for his practice manager. Logo alread...

I need a folder to put papers in when I am scheduling patients for surgery. The information is general, such as costs, consent forms etc. The folder is designed to give the patient these papers in a neat manner. The cover of the folder needs to use my brand and perhaps create some interest when it is sitting on their kitchen bench with visitors and family. I'll attach a typical template for a folder. It needs to be stylish, classic and professional, as I am about to operate on the person's eye. <br/>I would like my logo included. I'll also attach a photo which is on my website which might work to wrap around the folder. The website address is raybelford.com.au and you can see the way the image is used there on most of the pages as a banner. My profile photo could possibly used as well. Perhaps on the back, but if it looks strange then that is not necessary. The contact information need not be on the folder. Just Dr Ray Belford, Ophthalmic Surgeon. Finally, our brand slogan is. "The world's a beautiful place, see it clearly". This could also be on it. Again, this all needs to be professional looking. <br/>I've attached all our previous design jobs, 2 profile pictures, and the image that I think would work. Please also look at the website. <br/><br/>The second part of the project is to create a business card for my practice manager. Her name is Miriam Holtby<br/>It should include<br/>Miriam Holtby (BCom)<br/>Practice Manager for Dr Ray Belford<br/>Ophthalmic Surgeon <br/><br/>Then all the details which are on our current business card<br/><br/><br/><br/><br/>

Contact Information for Business Card

Just match the business cards I already have, but use the details above

Colors

Designer to choose colors to be used in the design.

```html
<!DOCTYPE html>
<html lang="en">
<head>
<meta charset="utf-8">
<title>Dr Ray Belford – Presentation Folder</title>
<link href="https://fonts.googleapis.com/css2?family=Open+Sans:wght@400;600;700&family=Arimo:wght@400&display=swap" rel="stylesheet">
<style>
  :root{
    --page:#ffffff;
    --edge:#6f6f6f;
    --brand-blue:#1f6fb5;
    --band-blue:#3f90cc;
    --light-blue:#19a9e5;
    --mid-blue:#1e8fd6;
    --deep-blue:#1673b9;
    --ink-grey:#555555;
    --photo-warm:#b98a4a;
    --photo-dark:#2e2c2c;
  }
  html,body{margin:0;padding:0;overflow:hidden;background:var(--page);}
  .canvas{position:relative;width:1200px;height:849px;overflow:hidden;background:var(--page);font-family:"Open Sans",Arial,sans-serif;}
  .folder-art{position:absolute;left:0;top:0;}
  .slogan{position:absolute;right:88px;top:438px;color:#fff;font-family:"Arimo",Arial,sans-serif;text-align:right;line-height:1;}
  .slogan__lead{font-size:20px;}
  .slogan__main{font-size:45px;margin-top:8px;letter-spacing:-0.5px;}
  .brand{position:absolute;display:flex;align-items:center;color:var(--brand-blue);}
  .brand__dot{border-radius:50%;background:var(--brand-blue);flex:none;}
  .brand__name{font-weight:700;line-height:1;}
  .brand__role{font-weight:700;color:#2a3f5a;line-height:1.2;}
  .brand__cred{color:#555;line-height:1.2;}
  .brand--back{left:76px;top:728px;}
  .brand--back .brand__dot{width:38px;height:38px;margin-right:24px;}
  .brand--back .brand__name{font-size:19px;}
  .brand--back .brand__role{font-size:7px;margin-top:3px;}
  .brand--back .brand__cred{font-size:6px;}
  .brand--front{left:846px;top:686px;}
  .brand--front .brand__dot{width:52px;height:52px;margin-right:34px;}
  .brand--front .brand__name{font-size:24px;}
  .brand--front .brand__role{font-size:9px;margin-top:4px;}
  .brand--front .brand__cred{font-size:7px;}
  .address{position:absolute;left:427px;top:727px;font-family:"Arimo",Arial,sans-serif;font-size:12.5px;color:var(--ink-grey);line-height:16px;}
  .address__web{margin-top:4px;letter-spacing:0.5px;}
  .footer-url{position:absolute;top:796px;width:562px;text-align:center;color:#fff;font-family:"Arimo",Arial,sans-serif;font-size:15px;letter-spacing:1px;}
  .footer-url--back{left:38px;}
  .footer-url--front{left:600px;}
</style>
</head>
<body>
<div class="canvas">
  <svg class="folder-art" width="1200" height="849" viewBox="0 0 1200 849" xmlns="http://www.w3.org/2000/svg">
    <defs>
      <linearGradient id="photoFill" x1="0" y1="0" x2="0" y2="1">
        <stop offset="0" stop-color="var(--photo-warm)"/>
        <stop offset="1" stop-color="var(--photo-dark)"/>
      </linearGradient>
      <linearGradient id="metalStrip" x1="0" y1="0" x2="0" y2="1">
        <stop offset="0" stop-color="#ffffff"/>
        <stop offset="1" stop-color="#a9a9a9"/>
      </linearGradient>
      <clipPath id="profileClip"><circle cx="175" cy="683" r="40"/></clipPath>
    </defs>

    <rect role="img" aria-label="Photograph: sunset over the open ocean seen from a boat, with a fishing rod at the right edge" x="38" y="27" width="1124" height="600" fill="url(#photoFill)"/>

    <polygon class="panel-white" fill="#fff" points="38,590 228,601 425,507 600,615 1030,643 1162,590 1162,822 38,822"/>

    <g class="zigzag-bands">
      <polygon fill="var(--light-blue)" points="38,508 228,601 38,590"/>
      <polygon fill="var(--mid-blue)" points="38,540 228,601 38,565"/>
      <polygon fill="var(--light-blue)" points="130,552 460,488 425,507 228,601"/>
      <polygon fill="var(--deep-blue)" points="228,601 350,540 425,507"/>
      <polygon fill="var(--deep-blue)" points="425,507 460,488 600,555 600,615"/>
      <polygon fill="var(--light-blue)" points="600,540 780,528 690,590 600,598"/>
      <polygon fill="var(--deep-blue)" points="690,590 780,528 1030,643"/>
      <polygon fill="var(--mid-blue)" points="600,598 690,590 1030,643 600,615"/>
      <polygon fill="var(--light-blue)" points="990,625 1162,510 1162,545"/>
      <polygon fill="var(--deep-blue)" points="1030,643 1162,545 1162,590"/>
    </g>

    <circle cx="175" cy="683" r="42" fill="var(--light-blue)"/>
    <rect role="img" aria-label="Portrait photograph of Dr Ray Belford" x="135" y="643" width="80" height="80" fill="#b9c6cf" clip-path="url(#profileClip)"/>

    <rect x="38" y="780" width="1124" height="12" fill="url(#metalStrip)"/>
    <rect x="38" y="790" width="1124" height="32" fill="var(--band-blue)"/>

    <line x1="600" y1="27" x2="600" y2="822" stroke="var(--edge)" stroke-width="0.8"/>
    <rect x="38" y="27" width="1124" height="795" fill="none" stroke="var(--edge)" stroke-width="0.8"/>
  </svg>

  <div class="slogan">
    <div class="slogan__lead">The world's a beautiful place,</div>
    <div class="slogan__main">see it clearly</div>
  </div>

  <div class="brand brand--back">
    <span class="brand__dot"></span>
    <div>
      <div class="brand__name">Dr Ray Belford</div>
      <div class="brand__role">Ophthalmic Surgeon</div>
      <div class="brand__cred">MBBS (Hons) MMed FRANZCO</div>
    </div>
  </div>

  <div class="address">
    <div>24 Harcourt Lane, Kingsford</div>
    <div>Western Australia 6012</div>
    <div class="address__web">www. raybelford.com.au</div>
  </div>

  <div class="brand brand--front">
    <span class="brand__dot"></span>
    <div>
      <div class="brand__name">Dr Ray Belford</div>
      <div class="brand__role">Ophthalmic Surgeon</div>
      <div class="brand__cred">MBBS (Hons) MMed FRANZCO</div>
    </div>
  </div>

  <div class="footer-url footer-url--back">www. raybelford.com.au</div>
  <div class="footer-url footer-url--front">www. raybelford.com.au</div>
</div>
</body>
</html>
```